Business Card for Leadership Coaching Business
Red Stone Leadership Coaching
Business Card for Leadership Coaching Business - Consulting
Creative Brief
Professional
Marla Pennington, CHRL
Leadership Coach
372 Fenwick Crescent, Oakville, Ontario L6K 3R2
marla@redstoneleadcoach.example
www.redstoneleadcoach.example
I am starting up a new business for leadership coaching. I have a great new logo and now I am looking for a great business card.
PRNGraphics PRNGraphics
Good afternoon. Can you post the logo you want to use on your card?

```html
<!DOCTYPE html>
<html lang="en">
<head>
<meta charset="utf-8">
<title>Red Stone Leadership Coaching – Business Card</title>
<link rel="stylesheet" href="https://fonts.googleapis.com/css2?family=Montserrat:wght@600&family=Tinos&display=swap">
<style>
  :root {
    --stage: #3a3a3a;
    --card-white: #ffffff;
    --navy: #1c4079;
    --blue: #1f5aa6;
    --sky: #3a8ad8;
    --ink: #3c3c3c;
    --rule: #b9c3cf;
  }
  * { margin: 0; padding: 0; box-sizing: border-box; }
  html, body { width: 1200px; height: 751px; overflow: hidden; }
  body { background: var(--stage); position: relative; }

  .card {
    position: absolute;
    top: 216px;
    width: 492px;
    height: 283px;
    border-radius: 16px;
    overflow: hidden;
  }
  .card--front { left: 91px; background: var(--card-white); }
  .card--back { left: 619px; background: var(--navy); }

  .card__wave { position: absolute; left: 0; top: 0; width: 100%; height: 100%; }

  .brand {
    position: absolute;
    font-family: "Montserrat", sans-serif;
    font-weight: 600;
    text-align: center;
    line-height: 1.05;
    letter-spacing: 0.5px;
  }
  .brand__name { display: block; font-size: 27px; }
  .brand__tag { display: block; font-size: 12.5px; letter-spacing: 0.6px; margin-top: 4px; }
  .card--front .brand { left: 14px; top: 92px; width: 210px; color: var(--blue); }
  .card--back .brand { left: 0; right: 0; top: 112px; color: var(--card-white); }
  .card--back .brand__name { font-size: 31px; }
  .card--back .brand__tag { font-size: 14.5px; }

  .card__divider {
    position: absolute;
    left: 231px; top: 48px;
    width: 1px; height: 144px;
    background: var(--rule);
  }

  .contact { position: absolute; left: 245px; top: 54px; }
  .contact__name {
    font-family: "Montserrat", sans-serif;
    font-weight: 600;
    font-size: 13px;
    letter-spacing: 0.8px;
    color: var(--blue);
    text-transform: uppercase;
  }
  .contact__role {
    font-family: "Montserrat", sans-serif;
    font-weight: 600;
    font-size: 10px;
    letter-spacing: 0.8px;
    color: var(--sky);
    text-transform: uppercase;
    margin-top: 7px;
  }
  .contact__lines {
    font-family: "Tinos", serif;
    font-size: 11.5px;
    line-height: 19px;
    color: var(--ink);
    margin-top: 10px;
  }
  .contact__gap { margin-top: 7px; }
</style>
</head>
<body>

  <section class="card card--front" aria-label="Business card front">
    <svg class="card__wave" viewBox="0 0 492 283" preserveAspectRatio="none" aria-hidden="true">
      <path d="M0 238 C 150 250, 330 235, 492 190 L 492 283 L 0 283 Z" fill="var(--navy)"/>
      <path d="M0 232 C 160 244, 330 226, 492 178" fill="none" stroke="var(--sky)" stroke-width="4"/>
      <path d="M0 222 C 170 236, 340 214, 492 168" fill="none" stroke="var(--rule)" stroke-width="1.5"/>
    </svg>

    <div class="brand">
      <span class="brand__name">RED STONE</span>
      <span class="brand__tag">LEADERSHIP COACHING</span>
    </div>

    <div class="card__divider"></div>

    <div class="contact">
      <p class="contact__name">Marla Pennington, CHRL</p>
      <p class="contact__role">Leadership Coach</p>
      <div class="contact__lines">
        <p>372 Fenwick Crescent</p>
        <p>Oakville, Ontario, L6K 3R2</p>
        <p class="contact__gap">905-555-0148</p>
        <p>marla@redstoneleadcoach.example</p>
        <p>www.redstoneleadcoach.example</p>
      </div>
    </div>
  </section>

  <section class="card card--back" aria-label="Business card back">
    <div class="brand">
      <span class="brand__name">RED STONE</span>
      <span class="brand__tag">LEADERSHIP COACHING</span>
    </div>
  </section>

</body>
</html>
```